Mobile Oil Change company needs a flyer to promote new business

We need a flyer to 1) print & handout and 2) email out to potential customers. We are a mobile oil change company that comes to our customer locations to perform the work instead of customers going to traditional oil change companies. We have a 21 point inspection with our oil change. (21 point inspection details will not be on the flyer). Would like to keep the flyer simple but creative. I'm attaching 1) the write-up we created, 2) our logo (logo color is dark teal on white but other combinations are included if you wanted to propose a different color combination), and 3) additional services we offer. Logo font is Alegreya Sans.
Would like the additional services listed with icons and brief descriptions (similar to attachment) without pricing. Company website for reference is www.brindlefleetcare.com.

Target Market(s)

Companies with many service vehicles such as Oil & Gas service companies, heating and air conditioning companies, utility companies, police departments, etc. Companies that prioritize convenience and maintenance first.

Font styles to use
Sans Serif

Colors
00a990

Requirements
Must have
• Simple but creative design with our logo at top of the flyer. Additional Services (details in document supplied) can be smaller and less prominent than other "main" content listed in the CONTENT document supplied.
Should not have
• Do not use animated character graphics in the flyer and limit (1) stock photos to A small area in the flyer.

```html
<!DOCTYPE html>
<html lang="en">
<head>
<meta charset="utf-8">
<title>Brindle Fleet Care – Hassle Free Oil Changes</title>
<link rel="stylesheet" href="https://fonts.googleapis.com/css2?family=Alegreya+Sans+SC:wght@700;800&family=Open+Sans:wght@600;700;800&family=Josefin+Sans:wght@600;700&display=swap">
<style>
:root{
  --teal-deep:#0b3532;
  --teal-dark:#0f403c;
  --teal-mid:#165650;
  --teal-accent:#00a990;
  --ink-teal:#1b4a48;
  --gold:#f2cf3a;
  --gold-line:#e0b93a;
  --cream:#f3ecd9;
  --white:#ffffff;
  --band-dark:#151515;
}
*{margin:0;padding:0;box-sizing:border-box}
html,body{width:927px;height:1200px;overflow:hidden;background:var(--white)}
.flyer{position:relative;width:927px;height:1200px;overflow:hidden;background:var(--teal-dark);font-family:"Open Sans",sans-serif}

/* hero */
.hero-photo{position:absolute;left:0;top:0;width:927px;height:380px;
  background:
   linear-gradient(160deg,rgba(17,82,74,.95) 0%,rgba(17,82,74,.85) 38%,rgba(17,82,74,0) 62%),
   linear-gradient(95deg,#1d2a26 0%,#3b3a2e 45%,#7a6646 70%,#4a3d28 85%,#1f1a12 100%);}
.brand{position:absolute;left:660px;top:52px;width:160px;color:var(--white);
  font-family:"Josefin Sans",sans-serif;font-weight:700;text-align:center;line-height:1}
.brand-name{display:block;font-size:40px;letter-spacing:1px}
.brand-sub{display:block;font-size:22px;letter-spacing:3px;margin-top:10px}
.headline{position:absolute;left:37px;top:190px;width:500px;height:158px;
  border-left:2px solid var(--cream);border-bottom:2px solid var(--cream);
  padding:12px 0 0 14px;color:var(--cream);font-family:"Josefin Sans",sans-serif;font-weight:600;line-height:1.1}
.headline-small{display:block;font-size:33px;letter-spacing:1px}
.headline-large{display:block;font-size:47px;letter-spacing:1px;margin-top:4px}

/* process band */
.process-band{position:absolute;left:0;top:378px;width:927px;height:177px;
  background:linear-gradient(180deg,#2a2a2a 0%,var(--band-dark) 60%,#222 100%)}
.process-card{position:absolute;left:159px;top:378px;width:612px;height:170px;background:var(--white);
  box-shadow:0 4px 14px rgba(0,0,0,.6);text-align:center;color:var(--ink-teal);
  font-family:"Alegreya Sans SC",sans-serif;font-weight:800;padding-top:18px;line-height:1.1}
.process-title{display:block;font-size:44px}
.process-sub{display:block;font-size:24px;margin-top:4px}
.process-end{display:block;font-size:42px;letter-spacing:1px;margin-top:4px}

/* steps banner */
.steps-banner{position:absolute;left:0;top:553px;width:927px;height:192px}
.steps-list{position:absolute;left:0;top:570px;width:927px;list-style:none;text-align:center;
  color:var(--ink-teal);font-family:"Alegreya Sans SC",sans-serif;font-weight:700;font-size:20px;line-height:26.5px}

/* lower area */
.lower{position:absolute;left:0;top:742px;width:927px;height:458px;background:var(--teal-dark)}
.services-panel{position:absolute;left:470px;top:742px;width:457px;height:458px;
  background:linear-gradient(180deg,#123f3b 0%,#0c3431 100%);box-shadow:-6px 0 14px rgba(0,0,0,.35)}

.promo{position:absolute;left:0;top:768px;width:470px;text-align:center;color:var(--gold);
  font-weight:800;line-height:1.12;letter-spacing:.5px}
.promo-lead{display:block;font-size:50px}
.promo-line{display:block;font-size:36px}
.promo-end{display:block;font-size:31px}
.dotted{display:block;width:370px;margin:16px auto;border-top:5px dotted var(--white)}
.promo-note{display:block;font-size:18px;font-weight:700;margin-top:4px}

.services-title{position:absolute;left:470px;top:760px;width:457px;text-align:center;
  color:var(--white);font-weight:700;font-size:24px}
.service{position:absolute;left:498px;width:420px;display:flex;align-items:flex-start;gap:16px;color:var(--white)}
.service svg{flex:0 0 38px;width:38px;height:38px}
.service p{font-size:13.4px;font-weight:700;line-height:1.35}
</style>
</head>
<body>
<div class="flyer">

  <div class="hero-photo" role="img" aria-label="Photo of a mechanic working in an open vehicle engine bay, tinted teal"></div>

  <div class="brand" aria-label="Brindle Fleet Care">
    <span class="brand-name">BRINDLE</span>
    <span class="brand-sub">FLEET CARE</span>
  </div>

  <h1 class="headline">
    <span class="headline-small">HASSLE FREE</span>
    <span class="headline-small">OIL CHANGES</span>
    <span class="headline-large">ON YOUR TERMS</span>
  </h1>

  <div class="process-band"></div>
  <div class="process-card">
    <span class="process-title">Our simple 5-step process</span>
    <span class="process-sub">lets you schedule an appointment and get service</span>
    <span class="process-end">to save time and money:</span>
  </div>

  <svg class="steps-banner" viewBox="0 0 927 192" aria-hidden="true">
    <polygon points="0,0 927,0 927,6 855,184 70,184 0,6" fill="#ffffff"/>
    <polyline points="0,6 70,186 855,186 927,6" fill="none" stroke="#e0b93a" stroke-width="4"/>
  </svg>
  <ol class="steps-list">
    <li>Call or email us to schedule service</li>
    <li>Our highly trained technicians come to you for service</li>
    <li>Service is performed quickly on your vehicle</li>
    <li>Pay agreed-upon pricing and receipt is emailed to you</li>
    <li>Services performed are tracked electronically</li>
    <li>and reminders created</li>
  </ol>

  <div class="lower"></div>
  <div class="services-panel"></div>

  <div class="promo">
    <span class="promo-lead">HIGH QUALITY</span>
    <span class="promo-line">SYNTHETIC OIL USED</span>
    <span class="promo-line">IS BEST SUITED FOR</span>
    <span class="promo-end">COMMERCIAL VEHICLES</span>
    <span class="dotted"></span>
    <span class="promo-line">SERVICE INCLUDES A</span>
    <span class="promo-line">21-POINT INSPECTION</span>
    <span class="dotted"></span>
    <span class="promo-note">ADDITIONAL SERVICES ARE AVAILABLE</span>
  </div>

  <h2 class="services-title">ADDITIONAL SERVICES</h2>

  <div class="service" style="top:812px">
    <svg viewBox="0 0 38 38" fill="none" stroke="#fff" stroke-width="2"><rect x="4" y="5" width="30" height="28"/><path d="M10 9v20M15 9v20M20 9v20M25 9v20M30 9v20"/></svg>
    <p>Maintain optimum engine performance.<br>Recommended every 15,000-30,000 miles.</p>
  </div>
  <div class="service" style="top:880px">
    <svg viewBox="0 0 38 38" fill="none" stroke="#fff" stroke-width="2"><rect x="7" y="4" width="22" height="30" rx="2"/><path d="M3 14q5-4 10 0t10 0t10 0M3 20q5-4 10 0t10 0t10 0M3 26q5-4 10 0t10 0t10 0"/></svg>
    <p>Maintain a clean A/C and fan system.<br>Recommended every 12 months or 15,000-25,000 miles.</p>
  </div>
  <div class="service" style="top:944px">
    <svg viewBox="0 0 38 38" fill="none" stroke="#fff" stroke-width="2"><path d="M4 24a15 15 0 0 1 30 0"/><path d="M19 30L9 14"/><circle cx="19" cy="30" r="2"/></svg>
    <p>Maintain excellent visibility on the road.<br>Recommended every 6-12 months.</p>
  </div>
  <div class="service" style="top:1004px">
    <svg viewBox="0 0 38 38" fill="none" stroke="#fff" stroke-width="2"><circle cx="19" cy="19" r="15"/><circle cx="19" cy="19" r="10"/><circle cx="19" cy="19" r="3"/><path d="M9 19h7M22 19h7M19 22v7"/></svg>
    <p>Maintain proper power steering system health.<br>Recommended every 30,000-60,000 miles.</p>
  </div>
  <div class="service" style="top:1065px">
    <svg viewBox="0 0 38 38" fill="none" stroke="#fff" stroke-width="2"><rect x="6" y="5" width="18" height="29" rx="2"/><rect x="10" y="9" width="10" height="8"/><path d="M24 14l6 4v12a2 2 0 0 0 4 0V12l-4-4"/></svg>
    <p>Clean your fuel system and injectors to<br>improve fuel economy.</p>
  </div>
  <div class="service" style="top:1134px">
    <svg viewBox="0 0 38 38" fill="none" stroke="#fff" stroke-width="2"><circle cx="19" cy="19" r="15"/><circle cx="19" cy="19" r="5"/><path d="M6 10a15 15 0 0 1 9-6"/><circle cx="19" cy="9" r="1.5"/><circle cx="29" cy="19" r="1.5"/><circle cx="19" cy="29" r="1.5"/><circle cx="9" cy="19" r="1.5"/></svg>
    <p>Maintan an excellent functional brake system.<br>Recommended every 2 years or 20,000 miles</p>
  </div>

</div>
</body>
</html>
```